Business cards for law firm with global theme

I'd like business cards with contact info for two offices. They should include the colors and font of the new logo design, which is a stylized globe with an "F" in it. The feel should be very modern and professional.

```html
<!DOCTYPE html>
<html lang="en">
<head>
<meta charset="utf-8">
<title>Veranto Law — Business Cards</title>
<link rel="stylesheet" href="https://fonts.googleapis.com/css2?family=Montserrat:wght@400;500;700&display=swap">
<style>
  :root {
    --navy: #053b6e;
    --sky: #0aa8e6;
    --paper: #ffffff;
    --ink: #4a4f57;
    --backdrop: #8d8f93;
    --font: "Montserrat", Arial, sans-serif;
  }
  * { box-sizing: border-box; margin: 0; padding: 0; }
  html, body {
    width: 1200px; height: 800px; overflow: hidden;
    background: var(--backdrop);
    font-family: var(--font);
  }
  .canvas {
    width: 1200px; height: 800px;
    display: flex; align-items: center; justify-content: center; gap: 40px;
  }
  .card {
    position: relative;
    width: 520px; height: 297px;
    border-radius: 22px;
    overflow: hidden;
    border-bottom: 3px solid var(--sky);
  }
  .card--front { background: var(--paper); }
  .card--back { background: var(--navy); }

  .edge-tab {
    position: absolute; left: 0; top: 126px;
    width: 8px; height: 40px; background: var(--navy);
  }
  .identity { position: absolute; left: 36px; top: 52px; }
  .identity__name {
    color: var(--navy); font-weight: 700; font-size: 26px;
    letter-spacing: 0.06em; text-transform: uppercase;
  }
  .identity__role {
    color: var(--sky); font-size: 14px; font-weight: 400;
    font-variant: small-caps; letter-spacing: 0.08em; margin-top: 2px;
  }
  .contacts {
    position: absolute; left: 36px; top: 128px;
    list-style: none; color: var(--ink);
    font-size: 11.5px; font-variant: small-caps; letter-spacing: 0.06em;
  }
  .contacts li { display: flex; align-items: flex-start; gap: 10px; margin-bottom: 5px; line-height: 1.3; }
  .contacts svg { width: 12px; height: 12px; flex: none; margin-top: 1px; fill: var(--sky); }

  .brand {
    position: absolute; left: 0; right: 0; top: 0; bottom: 0;
    display: flex; align-items: center; justify-content: center; gap: 18px;
  }
  .brand__dot { width: 56px; height: 56px; border-radius: 50%; background: var(--sky); }
  .brand__name {
    color: var(--paper); font-weight: 700; font-size: 40px;
    letter-spacing: 0.04em; text-transform: uppercase;
  }
</style>
</head>
<body>
<main class="canvas">

  <section class="card card--front" aria-label="Business card front">
    <span class="edge-tab"></span>
    <div class="identity">
      <h1 class="identity__name">Daniel Hart</h1>
      <p class="identity__role">Lawyer</p>
    </div>
    <ul class="contacts">
      <li>
        <svg viewBox="0 0 12 12" aria-hidden="true"><path d="M6 0a4 4 0 0 0-4 4c0 3 4 8 4 8s4-5 4-8a4 4 0 0 0-4-4zm0 5.6A1.6 1.6 0 1 1 6 2.4a1.6 1.6 0 0 1 0 3.2z"/></svg>
        <span>4820 Linden Avenue<br>Ridgefield, CT 06877</span>
      </li>
      <li>
        <svg viewBox="0 0 12 12" aria-hidden="true"><path d="M6 0a4 4 0 0 0-4 4c0 3 4 8 4 8s4-5 4-8a4 4 0 0 0-4-4zm0 5.6A1.6 1.6 0 1 1 6 2.4a1.6 1.6 0 0 1 0 3.2z"/></svg>
        <span>4820 Linden Avenue<br>Ridgefield, CT 06877</span>
      </li>
      <li>
        <svg viewBox="0 0 12 12" aria-hidden="true"><path d="M2.4 0.6l2 2-1.2 1.6c.8 1.7 2 2.9 3.6 3.6L8.4 6.6l2 2-1.4 2.6C4.6 11 1 7.4 0 3z"/></svg>
        <span>(555) 214-3087</span>
      </li>
      <li>
        <svg viewBox="0 0 12 12" aria-hidden="true"><path d="M3 0h6a1 1 0 0 1 1 1v10a1 1 0 0 1-1 1H3a1 1 0 0 1-1-1V1a1 1 0 0 1 1-1zm.5 1.5v8h5v-8z"/></svg>
        <span>(555) 214-3087</span>
      </li>
      <li>
        <svg viewBox="0 0 12 12" aria-hidden="true"><path d="M0 2h12v8H0zm1 1l5 4 5-4z"/></svg>
        <span>daniel@verantolaw.com</span>
      </li>
      <li>
        <svg viewBox="0 0 12 12" aria-hidden="true"><path d="M6 0a6 6 0 1 0 0 12A6 6 0 0 0 6 0zm0 1.2c.8.8 1.3 2.4 1.4 4.2H4.6C4.7 3.6 5.2 2 6 1.2zM4.6 6.6h2.8C7.3 8.4 6.8 10 6 10.8 5.2 10 4.7 8.4 4.6 6.6z"/></svg>
        <span>verantolaw.com</span>
      </li>
    </ul>
  </section>

  <section class="card card--back" aria-label="Business card back">
    <div class="brand">
      <span class="brand__dot"></span>
      <span class="brand__name">Veranto Law</span>
    </div>
  </section>

</main>
</body>
</html>
```